Readable, Vibrant Large Shop Front Poster for Tutoring School.

Uncluttered design for the windows of our Business.
It needs to be readable from a distance.
It will be split across two windows. I've uploaded a picture of the premises. The poster is unfortunately split in two- see the shopfront photo - It will be in the two Square windows where the balloons are now.
I've also uploaded our logo which will be used as signage/ on the roof and would like the posters to tie in with it.

What we want to stand out
Over all :
That we are a Tutoring School Specializing in Secondary/KTR Studies

On the left hand side:
- 1 hour lessons are $20 with no joining fees or contracts (casual week to week bookings)

The right hand side:
-Weekly Lessons no contracts
-Summer School
-Holiday Program
-Workshops
-KTR EXAM PREP

Need B0 size (1000mm x 1414mm)

Requirements
Must have
• It must have large clear writing.
Nice to have
• a border top and bottom of the logo swirls, We don't need the business name on this poster.
Should not have
• Not a fan of Purple or Lime Green.

```html
<!DOCTYPE html>
<html lang="en">
<head>
<meta charset="utf-8">
<title>Study Nest – Window Posters</title>
<link href="https://fonts.googleapis.com/css2?family=Montserrat:ital,wght@0,500;0,600;0,700;0,800;1,800&display=swap" rel="stylesheet">
<style>
  :root {
    --page: #ffffff;
    --navy-core: #12365a;
    --navy-mid: #0b2742;
    --navy-edge: #03111d;
    --ink: #ffffff;
    --accent: #f7a928;
    --rule: rgba(255, 255, 255, 0.75);
    --soft-ink: rgba(255, 255, 255, 0.85);
  }
  * { box-sizing: border-box; margin: 0; padding: 0; }
  html, body {
    width: 1200px;
    height: 852px;
    overflow: hidden;
    background: var(--page);
  }
  body {
    position: relative;
    font-family: "Montserrat", Arial, sans-serif;
    color: var(--ink);
  }
  .poster {
    position: absolute;
    top: 48px;
    width: 528px;
    height: 747px;
    background: radial-gradient(ellipse 60% 55% at 50% 52%, var(--navy-core) 0%, var(--navy-mid) 45%, var(--navy-edge) 100%);
    overflow: hidden;
  }
  .poster--offer { left: 33px; }
  .poster--programs { left: 628px; }

  .line {
    position: absolute;
    left: 0;
    width: 100%;
    text-align: center;
    line-height: 1;
    white-space: nowrap;
  }

  /* Offer poster */
  .brand-dot {
    position: absolute;
    left: 50%;
    top: 72px;
    width: 56px;
    height: 56px;
    margin-left: -28px;
    border-radius: 50%;
    background: var(--accent);
  }
  .brand-name {
    top: 156px;
    font-size: 29px;
    font-weight: 600;
    letter-spacing: 0.12em;
  }
  .offer-duration {
    top: 232px;
    font-size: 56px;
    font-weight: 500;
  }
  .offer-unit {
    top: 284px;
    font-size: 74px;
    font-weight: 700;
    letter-spacing: -0.01em;
  }
  .offer-price {
    top: 386px;
    font-size: 136px;
    font-weight: 800;
    font-style: italic;
    color: var(--accent);
    letter-spacing: -0.02em;
  }
  .offer-terms {
    font-size: 51px;
    font-weight: 500;
  }
  .offer-terms--one { top: 546px; }
  .offer-terms--two { top: 604px; }
  .school-focus {
    top: 688px;
    font-size: 19px;
    font-weight: 600;
    letter-spacing: 0.14em;
    color: var(--soft-ink);
  }

  /* Programs poster */
  .program-list {
    position: absolute;
    inset: 0;
    list-style: none;
  }
  .program {
    position: absolute;
    left: 0;
    width: 100%;
    text-align: center;
    font-size: 45px;
    font-weight: 700;
    line-height: 1;
    white-space: nowrap;
  }
  .program:nth-child(1) { top: 121px; }
  .program:nth-child(2) { top: 235px; }
  .program:nth-child(3) { top: 349px; }
  .program:nth-child(4) { top: 464px; }
  .program:nth-child(5) { top: 579px; letter-spacing: 0.01em; }
  .divider {
    position: absolute;
    left: 54px;
    width: 416px;
    border: 0;
    border-top: 2px dashed var(--rule);
  }
  .divider--1 { top: 206px; }
  .divider--2 { top: 318px; }
  .divider--3 { top: 430px; }
  .divider--4 { top: 542px; }
</style>
</head>
<body>
  <section class="poster poster--offer" aria-label="Lesson pricing">
    <span class="brand-dot" aria-hidden="true"></span>
    <p class="line brand-name">STUDY NEST</p>
    <p class="line offer-duration">1 hour</p>
    <p class="line offer-unit">lessons</p>
    <p class="line offer-price">$20</p>
    <p class="line offer-terms offer-terms--one">with no joining</p>
    <p class="line offer-terms offer-terms--two">fees or contracts</p>
    <p class="line school-focus">SECONDARY &amp; KTR TUTORING</p>
  </section>

  <section class="poster poster--programs" aria-label="Programs offered">
    <ul class="program-list">
      <li class="program">Weekly Lessons</li>
      <li class="program">Summer School</li>
      <li class="program">Holiday Program</li>
      <li class="program">Workshops</li>
      <li class="program">KTR EXAM PREP</li>
    </ul>
    <hr class="divider divider--1">
    <hr class="divider divider--2">
    <hr class="divider divider--3">
    <hr class="divider divider--4">
  </section>
</body>
</html>
```